Redesign Business Card

Redesign business card for Web Design company.

Add small "Web Design & Digital Marketing" under logo.

Colours and style based on our website -- see old business card attached.
Text and information in PDF document.

Design a new modern style.

Logo attached.

EDIT: Finals must include PSD or AI, and print-ready files. (according to specific pixel dimension and size)

```html
<!DOCTYPE html>
<html lang="en">
<head>
<meta charset="utf-8">
<title>Ridgeline Studio – Business Card</title>
<link rel="stylesheet" href="https://fonts.googleapis.com/css2?family=Montserrat:wght@400;500;600;700&display=swap">
<style>
  :root{
    --bg:#8e8f91;
    --card:#f4f4f4;
    --card-shade:#e4e4e4;
    --ink:#3a3a3c;
    --red:#c8202e;
    --dark:#2b2b2d;
    --dark-2:#404043;
    --light-text:#e9e9e9;
    --muted:#bdbdbd;
  }
  *{margin:0;padding:0;box-sizing:border-box}
  html,body{width:1200px;height:900px;overflow:hidden}
  body{background:var(--bg);font-family:"Montserrat",Arial,sans-serif;position:relative}
  .card{
    position:absolute;width:560px;height:320px;border-radius:22px;overflow:hidden;
    background:linear-gradient(135deg,var(--card) 0%,#ffffff 45%,var(--card-shade) 100%);
  }
  .card--front{left:70px;top:90px}
  .card--back{left:570px;top:480px}

  /* front */
  .front-brand{position:absolute;left:0;right:0;top:108px;display:flex;align-items:center;justify-content:center;gap:14px}
  .brand-square{width:34px;height:34px;background:var(--red)}
  .brand-name{font-weight:700;font-size:38px;letter-spacing:1px;color:var(--ink);text-transform:uppercase;line-height:1}
  .front-social{position:absolute;left:0;right:0;top:190px;display:flex;flex-direction:column;align-items:center;gap:8px}
  .social-square{width:20px;height:20px;background:var(--red);border-radius:3px}
  .social-handle{font-size:17px;color:#6a6a6c;font-weight:500}

  /* back */
  .back-art{position:absolute;inset:0}
  .back-brand{position:absolute;left:60px;top:52px}
  .back-brand .brand-name{font-size:36px}
  .tagline{margin-top:8px;font-size:16px;font-weight:500;color:var(--ink);letter-spacing:.3px}
  .contact{position:absolute;right:34px;top:130px;text-align:right;color:var(--light-text)}
  .contact-name{font-size:22px;font-weight:700;color:var(--muted);line-height:1.1}
  .contact-role{font-size:12px;color:var(--muted);margin-bottom:18px}
  .contact-line{display:flex;justify-content:flex-end;align-items:center;gap:8px;font-size:12.5px;line-height:24px}
  .contact-line svg{width:13px;height:13px;fill:var(--light-text)}
</style>
</head>
<body>

<section class="card card--front" aria-label="Business card front">
  <div class="front-brand">
    <span class="brand-square" aria-hidden="true"></span>
    <span class="brand-name">Ridgeline Studio</span>
  </div>
  <div class="front-social">
    <span class="social-square" aria-hidden="true"></span>
    <span class="social-handle">ridgelinestudioca</span>
  </div>
</section>

<section class="card card--back" aria-label="Business card back">
  <svg class="back-art" viewBox="0 0 560 320" aria-hidden="true">
    <path d="M560,112 C430,122 300,160 228,320 L560,320 Z" fill="var(--dark-2)" stroke="#ffffff" stroke-width="3"/>
    <path d="M560,124 C440,134 318,172 250,320 L560,320 Z" fill="var(--dark)"/>
    <circle cx="110" cy="340" r="95" fill="var(--red)"/>
  </svg>

  <div class="back-brand">
    <div class="brand-name">Ridgeline Studio</div>
    <div class="tagline">Web Design and Digital Marketing</div>
  </div>

  <div class="contact">
    <div class="contact-name">Marcus Hale</div>
    <div class="contact-role">Web Consultant</div>
    <div class="contact-line">555-014-2290
      <svg viewBox="0 0 24 24"><path d="M6.6 10.8a15 15 0 0 0 6.6 6.6l2.2-2.2a1 1 0 0 1 1-.25 11.4 11.4 0 0 0 3.6.57 1 1 0 0 1 1 1V20a1 1 0 0 1-1 1A17 17 0 0 1 3 4a1 1 0 0 1 1-1h3.5a1 1 0 0 1 1 1c0 1.25.2 2.45.57 3.6a1 1 0 0 1-.25 1z"/></svg>
    </div>
    <div class="contact-line">marcus@ridgelinestudio.ca
      <svg viewBox="0 0 24 24"><path d="M2 5h20v14H2z M4 7v.5l8 5 8-5V7l-8 5z" fill-rule="evenodd"/></svg>
    </div>
    <div class="contact-line">www.ridgelinestudio.ca
      <svg viewBox="0 0 24 24"><circle cx="12" cy="12" r="9" fill="none" stroke="#e9e9e9" stroke-width="2"/><path d="M3 12h18M12 3c3 3 3 15 0 18M12 3c-3 3-3 15 0 18" fill="none" stroke="#e9e9e9" stroke-width="1.6"/></svg>
    </div>
  </div>
</section>

</body>
</html>
```